Need to design a business card with logo

Hellow
we are a company ,
PT REKA LINTAS MANDIRI
looking for design of name card.
what we do is property development and management.
design preferable professional corporate look and feel.
corporate. color, pantone colour 289
information required is
company name " Reka Lintas Mandiri"
person name eg " Peter Hollis"
person title eg "secret agent"
address: 9 kestrel road , jakarta, indonesia
phone : +6221 5906471
mobile : 0813 294 615
email : peter@hollistran.com
website: www.peterhol.com
if you want to include logo in the design you are welcome and appreciated , or you can simply use the company name as the logo.
thanks
corporate , business person , show events, exhibition events ,etc
Business

```html
<!DOCTYPE html>
<html lang="en">
<head>
<meta charset="utf-8">
<title>Reka Lintas Mandiri – Business Card</title>
<link rel="stylesheet" href="https://fonts.googleapis.com/css2?family=Quicksand:wght@400;500;700&display=swap">
<style>
  :root {
    --navy: #0c2340;
    --navy-light: #1d3a6e;
    --silver: #e4e4e4;
    --silver-light: #f2f2f2;
    --ink: #3a3a3a;
    --ink-soft: #555;
    --rule: #bfbfbf;
    --white: #ffffff;
    --backdrop: #d9d6d2;
  }
  * { box-sizing: border-box; margin: 0; padding: 0; }
  html, body { width: 1200px; height: 723px; overflow: hidden; }
  body {
    background: var(--backdrop);
    font-family: "Quicksand", sans-serif;
    position: relative;
  }
  .card {
    position: absolute;
    top: 62px;
    width: 350px;
    height: 600px;
    overflow: hidden;
    box-shadow: 0 10px 30px rgba(0,0,0,.25);
  }
  /* Back side */
  .card-back {
    left: 200px;
    background: linear-gradient(160deg, var(--navy-light), var(--navy) 70%);
    color: var(--white);
  }
  .card-back .company-mark {
    position: absolute;
    top: 240px; left: 0; right: 0;
    text-align: center;
    font-weight: 700;
    font-size: 25px;
    letter-spacing: 1px;
  }
  .card-back .back-web {
    position: absolute;
    bottom: 50px; left: 0; right: 0;
    text-align: center;
    font-weight: 500;
    font-size: 16px;
  }
  /* Front side */
  .card-front {
    left: 650px;
    background: linear-gradient(180deg, var(--silver-light), var(--silver));
    color: var(--ink);
  }
  .company-name {
    position: absolute;
    top: 34px; left: 30px;
    font-weight: 700;
    font-size: 25px;
    color: var(--ink);
  }
  .name-box {
    position: absolute;
    top: 92px; left: 40px;
    width: 280px; height: 72px;
    background: var(--white);
    border-radius: 6px 0 0 6px;
    box-shadow: 0 2px 4px rgba(0,0,0,.15);
    padding: 12px 0 0 58px;
  }
  .name-box svg { position: absolute; left: 22px; top: 17px; }
  .person-name { font-weight: 700; font-size: 24px; line-height: 1.05; }
  .person-title { font-weight: 500; font-size: 15px; color: var(--ink-soft); }
  .accent-strip {
    position: absolute;
    top: 150px; right: 0;
    width: 30px; height: 40px;
    background: var(--navy);
  }
  .contact-list { position: absolute; top: 190px; left: 0; right: 0; list-style: none; }
  .contact-row {
    position: relative;
    height: 82px;
    border-top: 1px solid var(--rule);
    display: flex;
    align-items: center;
    padding-left: 100px;
    font-size: 15px;
    color: var(--ink-soft);
    line-height: 1.35;
  }
  .contact-row::before {
    content: "";
    position: absolute;
    top: -1px; left: 0;
    width: 32px; height: 2px;
    background: var(--navy);
  }
  .contact-row svg { position: absolute; left: 48px; top: 50%; transform: translateY(-50%); }
  .bottom-band {
    position: absolute;
    left: 0; right: 0; bottom: 0;
    height: 82px;
    background: var(--navy);
  }
</style>
</head>
<body>

<section class="card card-back" aria-label="Card back">
  <div class="company-mark">REKA LINTAS MANDIRI</div>
  <div class="back-web">www.peterhol.com</div>
</section>

<section class="card card-front" aria-label="Card front">
  <div class="company-name">Reka Lintas Mandiri</div>

  <div class="name-box">
    <svg width="24" height="24" viewBox="0 0 24 24" aria-hidden="true">
      <circle cx="12" cy="7" r="5" fill="#3a3a3a"/>
      <path d="M2 23c0-6 4.5-9 10-9s10 3 10 9z" fill="#3a3a3a"/>
    </svg>
    <div class="person-name">Peter Hollis</div>
    <div class="person-title">secret agent</div>
  </div>
  <div class="accent-strip"></div>

  <ul class="contact-list">
    <li class="contact-row">
      <svg width="18" height="18" viewBox="0 0 24 24" aria-hidden="true">
        <path d="M6.6 10.8a15 15 0 0 0 6.6 6.6l2.2-2.2a1 1 0 0 1 1-.25 11 11 0 0 0 3.6.6 1 1 0 0 1 1 1V20a1 1 0 0 1-1 1A17 17 0 0 1 3 4a1 1 0 0 1 1-1h3.5a1 1 0 0 1 1 1 11 11 0 0 0 .6 3.6 1 1 0 0 1-.25 1z" fill="#3a3a3a"/>
      </svg>
      <span>Phone : +6221 5906471<br>Mobile : 0813 294 615</span>
    </li>
    <li class="contact-row">
      <svg width="20" height="16" viewBox="0 0 20 16" aria-hidden="true">
        <rect x="0" y="0" width="20" height="16" fill="#3a3a3a"/>
        <path d="M0 0l10 8 10-8" fill="none" stroke="#e4e4e4" stroke-width="1.6"/>
      </svg>
      <span>peter@hollistran.com</span>
    </li>
    <li class="contact-row">
      <svg width="20" height="20" viewBox="0 0 20 20" aria-hidden="true" fill="none" stroke="#3a3a3a" stroke-width="1.6">
        <circle cx="10" cy="10" r="8.5"/>
        <ellipse cx="10" cy="10" rx="3.8" ry="8.5"/>
        <path d="M1.5 10h17M3 5.5h14M3 14.5h14"/>
      </svg>
      <span>www.peterhol.com</span>
    </li>
    <li class="contact-row">
      <svg width="16" height="22" viewBox="0 0 16 22" aria-hidden="true">
        <path d="M8 0a8 8 0 0 1 8 8c0 6-8 14-8 14S0 14 0 8a8 8 0 0 1 8-8z" fill="#3a3a3a"/>
        <circle cx="8" cy="8" r="3" fill="#e4e4e4"/>
      </svg>
      <span>9 kestrel road , jakarta,<br>indonesia</span>
    </li>
  </ul>

  <div class="bottom-band"></div>
</section>

</body>
</html>
```